DERMATOLOGY SERVICES ADDING CARE FOR sKIN, HAIR AND NAILS

postcard TO BE DISTRIBUTED TO RURAL COMMUNITY. medical CLINIC EXPANDING AND ADDING DERMATOLOGIST. TREATMENT OF skin PROBLEMS LIKE RASHES, SABIES, SKIN CANCERS, ROSACEA, PSORIASIS, ECZEMA, WOUND CARE, ACNE, ANTI-AGING AND OTHER BREAKDOWN OF SKIN.
SERVICES INCLUDED PLEASE SEE ATTACHED DOCUMENT
Updates

Project Deadline Extended
Reason: The designs we got few designers that sent designs and they are not what we want. We need to have more time

Target Market(s)

rural COMMUNITY

Industry/Entity Type

Medical

Font styles to use
Other font styles liked:
• LET DESIGNER CHOOSE

Requirements
Must have
• SKIN PROBLEMS AND DISORDERS MENTIONED IN THE ATTACHED FILES
• MEDICAL PROFESSION
• ADDRESS PHONE NUMBERS
• 482 N Larkin Avenue Wauchula, Florida 33870
• phone # 863-555-0182
• Marlow Tenbury Inc expanding its services
• mOST INSURANCE ACCEPTED INCLUDING MEDICARE
Nice to have
• ADD A LOGO
Should not have
• This is a US postcard to be left in restaurants, doctors offices RV park. No stamp or address line in the back

```html
<!DOCTYPE html>
<html lang="en">
<head>
<meta charset="utf-8">
<title>Dermatology Postcard</title>
<link href="https://fonts.googleapis.com/css2?family=Source+Sans+3:wght@300;400;600&family=Oswald:wght@500;600&family=Tinos:ital@0;1&display=swap" rel="stylesheet">
<style>
  :root {
    --bg: #e9ebee;
    --card: #ffffff;
    --blue: #1f8fc8;
    --aqua: #bfe6f2;
    --green: #6dbb2e;
    --teal: #2b9cc4;
    --ink: #333a40;
    --muted: #6b747c;
    --skin-a: #e9c3a6;
    --skin-b: #c98f72;
    --leaf-a: #9fcf5a;
    --leaf-b: #4f8f2a;
  }
  * { margin: 0; padding: 0; box-sizing: border-box; }
  html, body { width: 889px; height: 1200px; overflow: hidden; background: var(--bg); }
  body { position: relative; font-family: "Source Sans 3", Arial, sans-serif; color: var(--ink); }

  .postcard {
    position: absolute; left: 54px; width: 780px; height: 548px;
    background: var(--card); overflow: hidden;
    box-shadow: 0 6px 18px rgba(0,0,0,.18);
  }
  .postcard--front { top: 36px; }
  .postcard--back { top: 616px; }
  .postcard svg.art { position: absolute; inset: 0; }

  /* front */
  .clinic-name { position: absolute; left: 520px; top: 40px; display: flex; align-items: center; gap: 10px; }
  .clinic-name__dot { width: 14px; height: 14px; border-radius: 50%; background: var(--green); }
  .clinic-name__text { font-weight: 400; font-size: 18px; color: var(--muted); line-height: 1; }
  .headline { position: absolute; left: 486px; top: 98px; font-weight: 400; font-size: 44px; color: var(--blue); line-height: 1; }
  .locale { position: absolute; left: 488px; top: 148px; font-size: 20px; color: var(--ink); }
  .services-bar {
    position: absolute; left: 500px; top: 196px; width: 280px; height: 34px;
    background: var(--blue); color: #fff; font-family: "Oswald", sans-serif; font-weight: 500;
    font-size: 22px; letter-spacing: 1px; padding-left: 22px; line-height: 34px;
  }
  .services { position: absolute; right: 22px; top: 242px; list-style: none; text-align: right; font-family: "Tinos", serif; font-size: 17px; line-height: 22px; color: var(--ink); }
  .services li::after { content: "\2713"; color: var(--blue); margin-left: 6px; font-size: 14px; }
  .services li.services__wrap::after { content: none; }

  .drive-badge {
    position: absolute; left: 222px; top: 222px; width: 150px; height: 150px; border-radius: 50%;
    background: var(--green); color: #fff; border: 4px solid #fff;
    display: flex; flex-direction: column; align-items: center; justify-content: center; text-align: center;
  }
  .drive-badge__top { font-family: "Oswald", sans-serif; font-weight: 600; font-size: 17px; line-height: 1.1; }
  .drive-badge__main { font-family: "Tinos", serif; font-style: italic; font-size: 21px; line-height: 1.1; margin-top: 4px; }

  .conditions-bar {
    position: absolute; left: 70px; top: 396px; width: 690px; height: 78px;
    background: var(--blue); border-radius: 18px 0 0 18px; color: #fff; text-align: center;
  }
  .conditions-bar__lead { font-family: "Tinos", serif; font-style: italic; font-size: 28px; margin-top: 8px; }
  .conditions-bar__list { font-size: 15px; margin-top: 2px; }

  /* back */
  .profession { position: absolute; left: 28px; top: 262px; font-weight: 300; font-size: 34px; letter-spacing: 1px; color: var(--teal); text-transform: uppercase; }
  .expanding { position: absolute; left: 30px; top: 306px; font-size: 16px; color: var(--ink); }
  .insurance { position: absolute; left: 30px; top: 340px; font-family: "Oswald", sans-serif; font-weight: 500; font-size: 17px; color: var(--green); text-transform: uppercase; letter-spacing: .5px; }
  .contact { position: absolute; left: 30px; top: 374px; list-style: none; font-size: 15px; line-height: 22px; color: var(--ink); }
  .contact li { display: flex; align-items: center; gap: 6px; }
  .contact svg { width: 12px; height: 12px; fill: var(--teal); }
</style>
</head>
<body>

<section class="postcard postcard--front" aria-label="Postcard front">
  <svg class="art" width="780" height="548" viewBox="0 0 780 548">
    <defs>
      <linearGradient id="skinTone" x1="0" y1="0" x2="1" y2="1">
        <stop offset="0" stop-color="var(--skin-a)"/>
        <stop offset="1" stop-color="var(--skin-b)"/>
      </linearGradient>
    </defs>
    <path d="M0 0 H470 C430 150 330 330 0 420 Z" fill="url(#skinTone)" role="img" aria-label="Photo of a dermatologist examining a patient's shoulder with a magnifying lens"/>
    <path d="M470 0 C430 150 330 330 0 420 L0 440 C350 350 452 160 492 0 Z" fill="var(--blue)"/>
    <path d="M0 470 C150 430 260 470 400 548 L0 548 Z" fill="var(--aqua)"/>
    <path d="M430 548 C560 490 680 500 780 470 L780 548 Z" fill="var(--aqua)" opacity=".7"/>
  </svg>

  <div class="clinic-name">
    <span class="clinic-name__dot"></span>
    <span class="clinic-name__text">Marlow Tenbury Clinic</span>
  </div>
  <h1 class="headline">Dermatologist</h1>
  <p class="locale">now in Wauchula, Florida</p>
  <div class="services-bar">SERVICES</div>
  <ul class="services">
    <li>Skin exams</li>
    <li>Skin Disorders</li>
    <li>Skin Biopsies</li>
    <li>Mole and Skin Tag removal</li>
    <li class="services__wrap">Treatment of various skin</li>
    <li>hair and nail disease</li>
  </ul>

  <div class="drive-badge">
    <span class="drive-badge__top">NO NEED TO DRIVE</span>
    <span class="drive-badge__main">Care in your<br>community</span>
  </div>

  <div class="conditions-bar">
    <p class="conditions-bar__lead">Treat skin problems like</p>
    <p class="conditions-bar__list">skin cancers, rosacea, psoriasis, eczema, wound care and other breakdowns</p>
  </div>
</section>

<section class="postcard postcard--back" aria-label="Postcard back">
  <svg class="art" width="780" height="548" viewBox="0 0 780 548">
    <defs>
      <radialGradient id="leafTone" cx=".5" cy=".4" r=".7">
        <stop offset="0" stop-color="var(--leaf-a)"/>
        <stop offset="1" stop-color="var(--leaf-b)"/>
      </radialGradient>
    </defs>
    <path d="M0 0 H250 C255 120 200 210 0 230 Z" fill="url(#leafTone)" role="img" aria-label="Photo of a smiling woman with clear skin against a green background"/>
    <path d="M250 0 C255 120 200 210 0 230 L0 244 C215 224 270 130 264 0 Z" fill="var(--blue)"/>
    <path d="M264 0 C270 130 215 224 0 244 L0 256 C230 236 288 140 282 0 Z" fill="var(--aqua)"/>
  </svg>

  <h2 class="profession">Medical Profession</h2>
  <p class="expanding">Marlow Tenbury Inc expanding its services</p>
  <p class="insurance">Most insurance accepted including Medicare</p>
  <ul class="contact">
    <li><svg viewBox="0 0 12 12"><path d="M6 0a4 4 0 0 0-4 4c0 3 4 8 4 8s4-5 4-8a4 4 0 0 0-4-4zm0 5.5A1.5 1.5 0 1 1 6 2.5a1.5 1.5 0 0 1 0 3z"/></svg>482 N Larkin Avenue Wauchula, Florida 33870</li>
    <li><svg viewBox="0 0 12 12"><path d="M2.5 0.5l2 2-1 1.5c.8 1.7 2 2.9 3.5 3.5l1.5-1 2 2-1.5 2C4.5 10.5 1.5 7.5.5 2z"/></svg>863-555-0182</li>
  </ul>
</section>

</body>
</html>
```